New website for selling opensource software business to business

Website Quvo Software

The open source software industry has grown enormously in recent years. More and more customers from software companies choose an open source solution. Quvo Software is going to fulfill this increasing demand.

Core business

Reselling software subcriptions (business to business).

Side business

Selling consultancy and Training to customers

Goals:

- Binding of customers to K7 IT Group
- Sales of subscriptions to customer
- Enlarge network K7 IT Group
- USP: Sales of complete package, Software, consultancy and training

Products

There are a couple of products/ services that Quvo will provide. Below you will find an overview of the Products:

- Bluefox subscriptions
- Crater subscriptions
- Velmor products
- Customized consultancy for the customer
- Customized training for the customer

Style

Behind the website should be a cms system like pagecraft.

Target Market(s)

Business - Business

Industry/Entity Type

Business

Coding

Coded - Design and coding required

Number of Pages Required

5+ page

Font styles to use
Other font styles liked:
• Calibri

Colors
0355a3
3176b5
85abd2

Requirements
Must have
• Home page with large photo background, About us, contact page with safe option to request more info
• Portfolio pages:
• 4 pages with a product group each:
• 1. Blue fox
• 2. Craters
• 3. Velmor
• 4. Ourtrustwall
• 1. Blue Fox
• On top space for short info/bullets about Blue fox. Further, a grid with 8 columns. In the columns 2 buttons both lead to a popup. A popup for information and a popup for requesting a quote.
• 2. Crater:
• On top space for short info/bullets about Crater. Further, a grid with 3 columns. In the columns 2 buttons both lead to a popup. A popup for information and a popup for requesting a quote.
• 1. Velmor:
• On top space for short info/bullets about Velmor. Further, a grid with 4 columns. In the columns 2 buttons both lead to a popup. A popup for information and a popup for requesting a quote.
• 2. Ourtrustwall:
• On top space for short info/bullets about Ourtrustwall. Further, a grid with 2 columns. In the columns 2 buttons both lead to a popup. A popup for information and a popup for requesting a quote.

```html
<!DOCTYPE html>
<html lang="en">
<head>
<meta charset="utf-8">
<title>Ourtrustwall – Quvo Software</title>
<link rel="stylesheet" href="https://fonts.googleapis.com/css2?family=Poppins:wght@500;600&family=Roboto:wght@400;500&display=swap">
<style>
  :root {
    --hero-start: #1a8ad4;
    --hero-end: #0670b8;
    --white: #ffffff;
    --ink: #2a2a33;
    --body: #3c3c46;
    --accent: #1a82cc;
    --sky: #4ab3f0;
    --sky-soft: #eaf5fd;
    --purple: #3f2a84;
    --footer-bg: #f6f6f6;
    --rule: #dcdcdc;
    --badge: #ebebeb;
    --badge-text: #3f2a84;
  }
  * { box-sizing: border-box; margin: 0; padding: 0; }
  html, body { width: 1053px; height: 1200px; overflow: hidden; background: var(--white); }
  body { position: relative; font-family: 'Roboto', sans-serif; color: var(--body); }

  .hero {
    position: absolute; left: 0; top: 0; width: 1053px; height: 330px;
    background: linear-gradient(120deg, var(--hero-start) 0%, var(--hero-end) 100%);
  }
  .brand-badge {
    position: absolute; border-radius: 50%; background: var(--badge);
    display: flex; align-items: center; justify-content: center; text-align: center;
    font-family: 'Poppins', sans-serif; font-weight: 600; color: var(--badge-text);
    line-height: 1.1;
  }
  .hero .brand-badge { left: 75px; top: 20px; width: 78px; height: 78px; font-size: 11px; }
  .nav { position: absolute; top: 52px; left: 0; font-size: 11px; font-weight: 500; color: var(--white); text-transform: uppercase; }
  .nav a { position: absolute; white-space: nowrap; color: inherit; text-decoration: none; }
  .nav .active::after {
    content: ""; position: absolute; left: -6px; right: -6px; top: 20px; height: 2px; background: var(--white);
  }
  .cta-top {
    position: absolute; left: 823px; top: 43px; width: 149px; height: 32px; border-radius: 16px;
    background: var(--sky); color: var(--white); font-size: 10px; font-weight: 500;
    display: flex; align-items: center; justify-content: center; text-transform: uppercase;
  }
  .page-title {
    position: absolute; top: 166px; width: 100%; text-align: center;
    font-family: 'Poppins', sans-serif; font-weight: 600; font-size: 37px; color: var(--white);
  }
  .breadcrumb {
    position: absolute; top: 214px; width: 100%; text-align: center;
    font-size: 11.5px; font-weight: 500; color: var(--white);
  }

  .info .brand-badge { left: 342px; top: 430px; width: 102px; height: 102px; font-size: 13px; }
  .info-heading {
    position: absolute; left: 343px; top: 547px;
    font-family: 'Poppins', sans-serif; font-weight: 500; font-size: 24.5px; color: var(--ink);
  }
  .info-list { position: absolute; left: 343px; top: 598px; list-style: none; font-size: 12px; }
  .info-list li { position: relative; padding-left: 16px; height: 27.3px; }
  .info-list li::before {
    content: ""; position: absolute; left: 1px; top: 4px; width: 4px; height: 4px;
    border: 2px solid var(--accent); border-radius: 50%;
  }
  .btn {
    position: absolute; top: 754px; height: 32px; border-radius: 16px;
    display: flex; align-items: center; justify-content: center;
    font-size: 10px; font-weight: 500; text-transform: uppercase;
  }
  .btn-more { left: 340px; width: 134px; background: var(--purple); color: var(--white); }
  .btn-quote { left: 481px; width: 149px; background: var(--sky-soft); color: var(--sky); }

  .footer { position: absolute; left: 0; top: 869px; width: 1053px; height: 331px; background: var(--footer-bg); }
  .footer .brand-badge { left: 102px; top: 89px; width: 112px; height: 112px; font-size: 14px; }
  .footer-col { position: absolute; top: 71px; }
  .footer-col h3 {
    font-family: 'Poppins', sans-serif; font-weight: 500; font-size: 15px; color: var(--ink);
    letter-spacing: 0.5px; text-transform: uppercase; margin-bottom: 14px;
  }
  .footer-col ul { list-style: none; font-size: 11.2px; }
  .footer-col li { position: relative; padding-left: 11px; height: 30.5px; }
  .footer-col li::before {
    content: ""; position: absolute; left: 0; top: 4px; width: 3px; height: 3px;
    border-right: 1px solid var(--body); border-top: 1px solid var(--body); transform: rotate(45deg);
  }
  .col-links { left: 323px; }
  .col-account { left: 547px; }
  .col-support { left: 822px; }
  .footer-rule { position: absolute; left: 74px; top: 283px; width: 898px; height: 1px; background: var(--rule); }
  .copyright {
    position: absolute; top: 301px; width: 100%; text-align: center;
    font-family: 'Poppins', sans-serif; font-weight: 600; font-size: 10.5px; color: var(--ink);
  }
  .to-top {
    position: absolute; left: 972px; top: 265px; width: 36px; height: 36px; border-radius: 50%;
    background: var(--accent); display: flex; align-items: center; justify-content: center;
  }
</style>
</head>
<body>
  <header class="hero">
    <div class="brand-badge">Quvo<br>Software</div>
    <nav class="nav">
      <a style="left:490px">Home</a>
      <a style="left:554px">About Us</a>
      <a class="active" style="left:639px">Portfolio</a>
      <a style="left:730px">Contact Us</a>
    </nav>
    <div class="cta-top">Request More Info</div>
    <h1 class="page-title">Ourtrustwall</h1>
    <div class="breadcrumb">Home / Portfolio / Ourtrustwall</div>
  </header>

  <section class="info">
    <div class="brand-badge">Quvo<br>Software</div>
    <h2 class="info-heading">Information about Ourtrustwall</h2>
    <ul class="info-list">
      <li>Nullam dictum felis eu pede mollis pretium integer tincidunt cras.</li>
      <li>Dapibus vivamus elementum semper nisi aenean vulputate eleifend.</li>
      <li>Tellus aenean leo ligula porttitor eu consequat vitae.</li>
      <li>Aenean vulputate eleifend tellus aenean leo ligula porttitor eu conse.</li>
      <li>Blandit vel luctus pulvinar hendrerit id lorem maecenas.</li>
    </ul>
    <div class="btn btn-more">More Info</div>
    <div class="btn btn-quote">Request a Quote</div>
  </section>

  <footer class="footer">
    <div class="brand-badge">Quvo<br>Software</div>
    <div class="footer-col col-links">
      <h3>Useful Links</h3>
      <ul><li>Home</li><li>About Us</li><li>Portfolio</li><li>Contact Us</li></ul>
    </div>
    <div class="footer-col col-account">
      <h3>Create Account</h3>
      <ul><li>Sign-in</li><li>Pricing</li><li>Press</li><li>Jobs</li></ul>
    </div>
    <div class="footer-col col-support">
      <h3>Support</h3>
      <ul><li>Terms of Use</li><li>Privacy Policy</li><li>Support</li></ul>
    </div>
    <div class="footer-rule"></div>
    <div class="to-top">
      <svg width="10" height="10" viewBox="0 0 10 10"><path d="M2 6.5 L5 3.5 L8 6.5" fill="none" stroke="#ffffff" stroke-width="1.4"/></svg>
    </div>
    <div class="copyright">COPYRIGHT 2017 QUVO SOFTWARE | ALL RIGHT RESERVED</div>
  </footer>
</body>
</html>
```